Marlowen

I'm looking for business cards with the logo I've attached. I don't have an specific idea in mind and open to anything. All the usual info will be involved. Name, position in company, nr, email, address

```html
<!DOCTYPE html>
<html lang="en">
<head>
<meta charset="utf-8">
<title>Marlowen Business Cards</title>
<link rel="stylesheet" href="https://fonts.googleapis.com/css2?family=Montserrat:wght@500;700&family=Arimo:wght@400;700&display=swap">
<style>
  :root {
    --navy: #1b2f4e;
    --navy-light: #2c4566;
    --gold: #efb22f;
    --ink: #1b2f4e;
    --paper: #ffffff;
    --rule: #d6d9de;
    --stage: #2e2e2e;
  }
  * { margin: 0; padding: 0; box-sizing: border-box; }
  html, body { width: 1200px; height: 866px; overflow: hidden; }
  body {
    background: var(--stage);
    display: flex;
    flex-direction: column;
    align-items: center;
    justify-content: center;
    gap: 40px;
    font-family: "Arimo", Arial, sans-serif;
  }
  .card {
    position: relative;
    width: 640px;
    height: 366px;
    border-bottom: 7px solid var(--gold);
    overflow: hidden;
  }
  .card-front { background: var(--paper); color: var(--ink); }
  .card-back {
    background: linear-gradient(170deg, var(--navy) 55%, var(--navy-light) 100%);
    display: flex;
    align-items: center;
    justify-content: center;
  }
  .brand {
    font-family: "Montserrat", sans-serif;
    font-weight: 700;
    color: var(--gold);
    letter-spacing: 0.04em;
    display: flex;
    align-items: center;
    gap: 12px;
    white-space: nowrap;
  }
  .brand-mark { width: 12px; height: 12px; background: var(--gold); flex: none; }
  .card-front .brand { position: absolute; right: 44px; top: 116px; font-size: 36px; }
  .card-back .brand { font-size: 58px; }
  .contact {
    position: absolute;
    left: 40px;
    top: 92px;
  }
  .person-name {
    font-family: "Montserrat", sans-serif;
    font-weight: 700;
    color: var(--gold);
    font-size: 21px;
    letter-spacing: 0.03em;
    text-transform: uppercase;
  }
  .person-role {
    font-size: 13px;
    letter-spacing: 0.06em;
    text-transform: uppercase;
    margin: 4px 0 14px;
  }
  .contact-list { list-style: none; font-size: 13px; letter-spacing: 0.04em; text-transform: uppercase; }
  .contact-list li { display: flex; align-items: center; gap: 8px; line-height: 21px; }
  .contact-list svg { width: 13px; height: 13px; flex: none; }
  .accent { color: var(--gold); }
  .divider {
    position: absolute;
    left: 240px;
    right: 40px;
    top: 232px;
    border-top: 1px solid var(--rule);
  }
  .address {
    position: absolute;
    right: 40px;
    top: 250px;
    text-align: right;
    font-size: 13px;
    line-height: 19px;
    letter-spacing: 0.05em;
    text-transform: uppercase;
    font-style: normal;
  }
</style>
</head>
<body>
  <section class="card card-front">
    <div class="brand"><span class="brand-mark"></span>MARLOWEN</div>
    <div class="contact">
      <p class="person-name">Elias Brandt</p>
      <p class="person-role">Managing Director</p>
      <ul class="contact-list">
        <li>
          <svg viewBox="0 0 16 16"><path fill="#efb22f" d="M3.6 1.5l2.4 2.6-1.3 2a9 9 0 0 0 5.2 5.2l2-1.3 2.6 2.4-1.6 2.1C7 14.3 1.7 9 1.5 3.1z"/></svg>
          044-318 207 645
        </li>
        <li>
          <svg viewBox="0 0 16 16"><rect x="1" y="3" width="14" height="10" fill="#efb22f"/><path d="M1.5 3.5L8 9l6.5-5.5" fill="none" stroke="#fff" stroke-width="1.4"/></svg>
          hello@marlowen.com
        </li>
        <li>
          <svg viewBox="0 0 16 16"><g fill="none" stroke="#efb22f" stroke-width="1.5"><circle cx="8" cy="8" r="6.5"/><ellipse cx="8" cy="8" rx="2.8" ry="6.5"/><path d="M1.5 8h13"/></g></svg>
          <span>www.<span class="accent">marlowenstudio</span>.com</span>
        </li>
      </ul>
    </div>
    <div class="divider"></div>
    <address class="address">87, Larkspur Row, Harbour Quarter<br>30218, Eastvale</address>
  </section>

  <section class="card card-back">
    <div class="brand"><span class="brand-mark"></span>MARLOWEN</div>
  </section>
</body>
</html>
```